Quolvex custom business card design

Need a authentic, innovative business card design for a new mobile app business. I am uploading a few screen images from our app for you to view. I would like app design theme to match business card design. I can also send logo images.

```html
<!DOCTYPE html>
<html lang="en">
<head>
<meta charset="utf-8">
<title>Quolvex business card</title>
<link href="https://fonts.googleapis.com/css2?family=Montserrat:wght@700;800;900&family=Open+Sans:wght@400;600&display=swap" rel="stylesheet">
<style>
  :root {
    --purple: #5f0089;
    --ink: #1e1e1e;
    --grey-text: #555555;
    --lavender: #ece4f3;
    --mist: #e6e6e6;
    --paper: #ffffff;
    --backdrop: #e9e9ea;
  }
  * { box-sizing: border-box; margin: 0; padding: 0; }
  html, body {
    width: 1200px; height: 900px; overflow: hidden;
    background: var(--backdrop);
  }
  .canvas { position: relative; width: 1200px; height: 900px; }

  .card {
    position: absolute;
    width: 560px; height: 320px;
    border-radius: 26px;
    overflow: hidden;
  }

  /* Back of card */
  .card--back {
    left: 80px; top: 110px;
    background: var(--purple);
    display: flex; flex-direction: column; align-items: center; justify-content: center;
    gap: 14px;
  }
  .brand-mark {
    width: 108px; height: 108px; border-radius: 50%;
    background: var(--paper);
  }
  .card--back .wordmark {
    font-family: "Montserrat", sans-serif;
    font-weight: 900; font-size: 48px; color: var(--paper);
    letter-spacing: 0.5px;
  }

  /* Front of card */
  .card--front {
    left: 560px; top: 470px;
    background: var(--paper);
  }
  .card--front .backdrop-circle {
    position: absolute; right: -70px; top: -90px;
    width: 330px; height: 330px; border-radius: 50%;
    background: var(--lavender);
  }
  .brand-row {
    position: absolute; left: 40px; top: 66px;
    display: flex; align-items: center; gap: 16px;
  }
  .brand-row .brand-dot {
    width: 62px; height: 62px; border-radius: 50%;
    background: var(--ink);
  }
  .brand-row .wordmark {
    font-family: "Montserrat", sans-serif;
    font-weight: 900; font-size: 46px; color: var(--ink);
  }

  .person { position: absolute; left: 40px; top: 160px; }
  .person .name {
    font-family: "Montserrat", sans-serif;
    font-weight: 800; font-size: 19px; color: var(--purple);
    letter-spacing: 0.5px; text-transform: uppercase;
  }
  .person .role {
    font-family: "Open Sans", sans-serif;
    font-size: 14px; color: var(--grey-text); margin-top: 1px;
  }
  .contact-list { list-style: none; margin-top: 8px; }
  .contact-list li {
    display: flex; align-items: center; gap: 8px;
    font-family: "Open Sans", sans-serif;
    font-size: 14.5px; line-height: 20px; color: var(--grey-text);
  }
  .contact-list svg { width: 12px; height: 12px; fill: var(--purple); flex: none; }

  .address {
    position: absolute; right: 34px; top: 170px;
    font-family: "Open Sans", sans-serif;
    font-size: 14.5px; line-height: 20px; color: var(--grey-text);
    text-align: right;
  }
</style>
</head>
<body>
<main class="canvas">

  <section class="card card--back" aria-label="Card back">
    <div class="brand-mark"></div>
    <div class="wordmark">Quolvex</div>
  </section>

  <section class="card card--front" aria-label="Card front">
    <div class="backdrop-circle"></div>

    <div class="brand-row">
      <div class="brand-dot"></div>
      <div class="wordmark">Quolvex</div>
    </div>

    <div class="person">
      <div class="name">Daniel <span>Harlow</span></div>
      <div class="role">Managing Director</div>
      <ul class="contact-list">
        <li>
          <svg viewBox="0 0 12 12" aria-hidden="true"><path d="M1 3c0-1 1-2 2-2h6c1 0 2 1 2 2v1H8V3H4v1H1zM2 5h8l1 5H1z"/></svg>
          044-987 650 214
        </li>
        <li>
          <svg viewBox="0 0 12 12" aria-hidden="true"><path d="M3 0h6v12H3zM4 1.5v8h4v-8z"/></svg>
          044-987 650 318
        </li>
        <li>
          <svg viewBox="0 0 12 12" aria-hidden="true"><path d="M0 2h12v8H0zM1 3l5 4 5-4z" fill-rule="evenodd"/></svg>
          info@quolvexapp.com
        </li>
        <li>
          <svg viewBox="0 0 12 12" aria-hidden="true"><circle cx="6" cy="6" r="6"/></svg>
          www.quolvexapp.com
        </li>
      </ul>
    </div>

    <address class="address" style="font-style: normal;">
      48 Linden Row, Suite 4<br>
      Harbourton, 560021
    </address>
  </section>

</main>
</body>
</html>
```